Events floral designer business needs a logo design

I need a logo design for my floral design business called tender thorns.
i am inspired by nature and the simplicity of its beauty, whilst upcycling and recycling materials to reduce waste and impact on our environment.
I would like the design to be printed on recycled brown cardboard so i would like a simple but striking design of a bold black ivy vine or gnarly magnolia or tree branch with lower case old school type writer font.

Target Market(s)

Anyone requiring floral additions for their event

Industry/Entity Type

Business

Contact Information for Business Card

mara hollis
floral designer/creator
0418657203
mara@tenderthorns.com
tenderthorns.com

Font styles to use
Other font styles liked:
• lower case type writer

Colors
000000

Requirements
Must have
• simplicity but boldness
• Black typewriter font and bold picture with my details
Nice to have
• as above
Should not have
• colour

```html
<!DOCTYPE html>
<html lang="en">
<head>
<meta charset="utf-8">
<title>tender thorns – business card</title>
<link href="https://fonts.googleapis.com/css2?family=Courier+Prime&display=swap" rel="stylesheet">
<style>
  :root {
    --ink: #1a1a1a;
    --paper: #ffffff;
    --artwork-dark: #2b2b2b;
    --artwork-mid: #6a6a6a;
  }
  html, body {
    margin: 0;
    padding: 0;
    overflow: hidden;
    background: var(--paper);
  }
  .card {
    position: relative;
    width: 1200px;
    height: 670px;
    background: var(--paper);
    color: var(--ink);
    font-family: "Courier Prime", "Courier New", monospace;
    font-weight: 400;
    overflow: hidden;
  }
  .brand-name {
    position: absolute;
    top: 42px;
    left: 0;
    width: 100%;
    margin: 0;
    text-align: center;
    font-size: 118px;
    font-weight: 400;
    line-height: 1;
    letter-spacing: 0;
  }
  .flower-artwork {
    position: absolute;
    left: 383px;
    top: 182px;
    width: 390px;
    height: 360px;
    border-radius: 46% 54% 42% 58% / 40% 44% 56% 60%;
    background: radial-gradient(ellipse at 50% 40%, var(--artwork-mid) 0%, var(--artwork-dark) 70%);
  }
  .person {
    position: absolute;
    left: 31px;
    top: 530px;
    margin: 0;
    font-size: 31px;
    line-height: 48px;
  }
  .contact {
    position: absolute;
    right: 30px;
    top: 490px;
    margin: 0;
    text-align: right;
    font-size: 31px;
    line-height: 46px;
    font-style: normal;
  }
  .person span,
  .contact span {
    display: block;
    white-space: nowrap;
  }
</style>
</head>
<body>
  <main class="card">
    <h1 class="brand-name">tender thorns</h1>

    <div class="flower-artwork" role="img" aria-label="Bold black sketched magnolia flower with spiky, thorny leaves and stem"></div>

    <p class="person">
      <span class="person-name">Mara Hollis</span>
      <span class="person-role">Floral designer/creator</span>
    </p>

    <address class="contact">
      <span class="contact-phone">0418657203</span>
      <span class="contact-email">mara@tenderthorns.com</span>
      <span class="contact-web">tenderthorns.com</span>
    </address>
  </main>
</body>
</html>
```